Layout for site fence advertising - length approx. 250 cm x 125 cm

The advertising will later be printed on a PVC film and used for events or on sports fields.

Main services :
Your regional contact at
Real estate and business financing
independent insurance advice

```html
<!DOCTYPE html>
<html lang="de">
<head>
<meta charset="utf-8">
<title>Arnholt Vermögensberatung – Bauzaunbanner</title>
<link rel="stylesheet" href="https://fonts.googleapis.com/css2?family=Bebas+Neue&family=Comfortaa:wght@700&family=Montserrat:wght@400&display=swap">
<style>
  :root {
    --page-bg: #dcdddf;
    --white: #ffffff;
    --brand-blue: #2a5ca8;
    --service-band: #dcdcdc;
    --text-grey: #6a6a6a;
    --dark-grey: #5a5a5a;
    --photo-dark: #3b2e2a;
    --photo-mid: #6b5a52;
  }
  * { margin: 0; padding: 0; box-sizing: border-box; }
  html, body {
    width: 1200px; height: 801px; overflow: hidden;
    background: var(--page-bg);
  }
  .banner {
    position: absolute; left: 0; top: 100px;
    width: 1200px; height: 601px;
    background: var(--white);
    overflow: hidden;
  }
  .portrait {
    position: absolute; left: 883px; top: 0;
    width: 317px; height: 425px;
    background:
      linear-gradient(90deg, var(--white) 0%, rgba(255,255,255,0) 12%),
      radial-gradient(ellipse at 55% 30%, #c99882 0%, #a07a68 22%, var(--photo-mid) 45%, var(--photo-dark) 100%);
  }
  .brand {
    position: absolute; left: 0; top: 0; width: 883px; height: 291px;
  }
  .brand-mark { position: absolute; left: 84px; top: 63px; }
  .brand-divider {
    position: absolute; left: 309px; top: 60px;
    width: 5px; height: 212px; background: var(--dark-grey);
  }
  .brand-name {
    position: absolute; left: 330px; top: 122px;
    font-family: "Comfortaa", sans-serif; font-weight: 700;
    font-size: 31px; color: var(--brand-blue); white-space: nowrap;
  }
  .brand-tagline {
    position: absolute; left: 330px; top: 164px;
    font-family: "Comfortaa", sans-serif; font-weight: 700;
    font-size: 25px; color: var(--dark-grey); white-space: nowrap;
  }
  .services {
    position: absolute; left: 0; top: 291px;
    width: 1200px; height: 134px; background: var(--service-band);
  }
  .service {
    position: absolute; top: 28px;
    display: flex; align-items: center; gap: 18px;
  }
  .service--financing { left: 92px; }
  .service--insurance { left: 522px; }
  .service-text {
    font-family: "Montserrat", sans-serif; font-weight: 400;
    font-size: 29px; line-height: 36px; color: var(--text-grey);
    white-space: nowrap;
  }
  .contact-bar {
    position: absolute; left: 0; top: 425px;
    width: 1200px; height: 153px; background: var(--brand-blue);
    display: flex; align-items: center;
    font-family: "Bebas Neue", sans-serif; color: var(--white);
    font-size: 90px; line-height: 1; white-space: nowrap;
  }
  .contact-phone { position: absolute; left: 74px; top: 34px; }
  .contact-sep {
    position: absolute; left: 524px; top: 35px;
    width: 6px; height: 88px; background: var(--white);
  }
  .contact-web { position: absolute; left: 593px; top: 34px; letter-spacing: 0.5px; }
</style>
</head>
<body>
<main class="banner">
  <div class="portrait" role="img" aria-label="Portraitfoto des Beraters im dunklen Sakko vor unscharfem Innenraum"></div>

  <header class="brand">
    <svg class="brand-mark" width="210" height="210" viewBox="0 0 210 210" aria-hidden="true">
      <circle cx="105" cy="105" r="100" fill="none" stroke="var(--brand-blue)" stroke-width="6"/>
    </svg>
    <div class="brand-divider"></div>
    <p class="brand-name">Arnholt Vermögensberatung GmbH</p>
    <p class="brand-tagline">Finanzieren, Versichern, Vorsorgen</p>
  </header>

  <section class="services">
    <div class="service service--financing">
      <svg width="62" height="62" viewBox="0 0 62 62" aria-hidden="true">
        <g fill="var(--brand-blue)">
          <rect x="5" y="4" width="22" height="52"/>
          <rect x="30" y="22" width="12" height="34"/>
          <rect x="44" y="14" width="13" height="42"/>
          <rect x="0" y="57" width="62" height="3"/>
        </g>
        <g fill="var(--service-band)">
          <rect x="9" y="9" width="5" height="5"/><rect x="18" y="9" width="5" height="5"/>
          <rect x="9" y="19" width="5" height="5"/><rect x="18" y="19" width="5" height="5"/>
          <rect x="9" y="29" width="5" height="5"/><rect x="18" y="29" width="5" height="5"/>
          <rect x="34" y="28" width="4" height="26"/>
          <rect x="48" y="20" width="4" height="34"/>
        </g>
      </svg>
      <p class="service-text">Real estate and<br>Business Financing</p>
    </div>
    <div class="service service--insurance">
      <svg width="62" height="62" viewBox="0 0 62 62" aria-hidden="true">
        <g fill="var(--brand-blue)">
          <path d="M8 26 A23 23 0 0 1 54 26 Z"/>
          <rect x="29.5" y="4" width="3" height="6"/>
          <rect x="29.5" y="26" width="3" height="16"/>
          <path d="M2 50 L14 40 Q20 36 28 38 L40 40 Q44 42 40 45 L30 45 L42 46 L56 36 Q61 35 58 41 L46 54 Q42 58 34 58 L12 58 L6 62 L2 58 Z"/>
        </g>
      </svg>
      <p class="service-text">Independent<br>Insurance Advice</p>
    </div>
  </section>

  <footer class="contact-bar">
    <span class="contact-phone">123 465 7890</span>
    <span class="contact-sep" aria-hidden="true"></span>
    <span class="contact-web">WWW.WEBSITE.COM</span>
  </footer>
</main>
</body>
</html>
```